Consulting company, design, Interior design in commercial real estate (Tertiai sector *

Company name: VORANDEL: from the Greek Evexia well-being, was born from a desire to combine well-being and work. By the choice of design, materials, design and furniture, everything is thought from this perspective

Logo: Essay with Möbius Ribbon and / or with the infinite acronym / and or triangle ...
Sentences to write:
"The exclusive partner for your development projects"
"Consulting - Design - Construction"
"We manage EVERYTHING for you"

On the back: Photo (attached; if photo is not clear, another photo can be provided) with company name and "VORANDEL, Excellence and reliability"
My name / First name: provided later (double name), Manager
Address: supplied later
Tel: supplied later
Website: www. vorandel.com
Colors: Black, gold and white. Other admissible colors
See attached files

Real estate business

Nom de l'entreprise : VORANDEL : du grec Evexia bien être, est né d'une volonté de faire rimer bien être et travail. Par le choix de la conception, des matériaux, du design et du mobilier, tout est pensé dans cette optique

Logo : Essai avec Ruban de Möbius et /ou avec le sigle infini / et ou triangle...
Phrases à inscrire :
"Le partenaire exclusif de vos projets d'aménagement"
"Conseil - Conception - Construction"
"Nous gérons TOUT pour vous"

Au verso : Photo (ci-jointe ; si photo pas nette, une autre photo peut être fournie) avec nom de l'entreprise et Mention "VORANDEL, Excellence et fiabilité"
Mon nom / Prénom : fourni ultérieurement (prénom double), Gérant
Adresse : fourni ultérieurement
Tél : fourni ultérieurement
Site Web : www. vorandel.com
Couleurs : Noir, doré et blanc. Autre couleurs recevables
Voir fichiers ci-joint

• My project must be simple, clear, neat and design.
The business card must catch the customer

```html
<!DOCTYPE html>
<html lang="en">
<head>
<meta charset="UTF-8">
<title>Vorandel – Business Card</title>
<link href="https://fonts.googleapis.com/css2?family=Poppins:wght@300;400;500;600&display=swap" rel="stylesheet">
<style>
  :root {
    --stage: #1b1b1d;
    --card: #232325;
    --gold: #d9ad4a;
    --gold-deep: #a97c24;
    --gold-light: #f6dc86;
    --white: #f3f1ec;
    --soft-white: #d8d6d0;
  }
  * { margin: 0; padding: 0; box-sizing: border-box; }
  html, body { width: 1200px; height: 800px; overflow: hidden; background: var(--stage); }
  body {
    display: flex; align-items: center; justify-content: center; gap: 40px;
    font-family: "Poppins", sans-serif; color: var(--white);
  }
  .card {
    position: relative; width: 540px; height: 309px;
    background: var(--card); overflow: hidden;
    box-shadow: 0 18px 40px rgba(0,0,0,.55);
  }
  .card__band {
    position: absolute; left: 0; right: 0; bottom: 0; height: 7px;
    background: linear-gradient(90deg, var(--gold-deep), var(--gold-light) 45%, var(--gold) 70%, var(--gold-deep));
  }
  .rule { height: 1px; background: var(--gold); }

  /* Front */
  .front { display: flex; }
  .front__brand {
    width: 220px; display: flex; flex-direction: column; align-items: center; justify-content: center; gap: 16px;
    padding-bottom: 10px;
  }
  .brand-dot { width: 70px; height: 70px; border-radius: 50%; background: var(--gold); }
  .brand-name {
    font-family: "Poppins", sans-serif; font-weight: 500; font-size: 26px; letter-spacing: 4px; color: var(--gold);
  }
  .front__message {
    flex: 1; padding: 34px 36px 0 10px; display: flex; flex-direction: column;
  }
  .slogan { font-weight: 300; font-size: 17px; letter-spacing: 2.5px; line-height: 1.3; text-transform: uppercase; }
  .slogan strong { font-weight: 600; color: var(--gold); }
  .slogan__tail { display: block; padding-left: 70px; }
  .front__message .rule { margin: 9px 0 9px 40px; }
  .services { font-weight: 300; font-size: 11.5px; letter-spacing: 2.5px; line-height: 1.3; text-transform: uppercase; padding-left: 60px; }
  .services span { display: block; }
  .services span:nth-child(2) { padding-left: 26px; }
  .partner { font-weight: 500; font-size: 11px; letter-spacing: 1px; line-height: 1.45; text-transform: uppercase; padding-left: 20px; }
  .partner span { display: block; }
  .partner span:nth-child(2) { padding-left: 54px; }
  .partner span:nth-child(3) { padding-left: 30px; }
  .website-spaced { font-size: 11px; letter-spacing: 9px; padding-left: 10px; margin-top: 2px; }

  /* Back */
  .back { padding: 40px 40px 0; }
  .back__wordmark { font-family: "Poppins", sans-serif; font-weight: 500; font-size: 50px; letter-spacing: 7px; color: var(--gold); line-height: 1; padding-left: 18px; }
  .back__motto { font-weight: 300; font-size: 12px; letter-spacing: 3px; text-transform: uppercase; color: var(--soft-white); padding-left: 22px; margin-top: 12px; }
  .person { display: flex; align-items: center; gap: 12px; margin-top: 18px; }
  .person .rule { flex: 1; }
  .person__text { text-align: right; line-height: 1.15; }
  .person__name { font-size: 17px; font-weight: 400; letter-spacing: .5px; }
  .person__name b { font-weight: 600; }
  .person__role { font-size: 11px; letter-spacing: 1.5px; color: var(--gold); }
  .contact { display: flex; align-items: center; gap: 18px; margin-top: 16px; padding-left: 70px; }
  .contact__address { font-size: 12.5px; line-height: 1.45; color: var(--white); text-align: right; }
  .contact__divider { width: 1px; height: 40px; background: var(--gold); }
  .contact__list { list-style: none; font-size: 12.5px; line-height: 1.6; }
  .contact__list li { display: flex; align-items: center; gap: 8px; }
  .contact__list svg { width: 12px; height: 12px; fill: var(--gold); }
</style>
</head>
<body>
  <section class="card front">
    <div class="front__brand">
      <span class="brand-dot"></span>
      <span class="brand-name">VORANDEL</span>
    </div>
    <div class="front__message">
      <p class="slogan">We manage <strong>everything</strong><span class="slogan__tail">for you</span></p>
      <div class="rule"></div>
      <p class="services"><span>Consulting</span><span>Design</span><span>Construction</span></p>
      <div class="rule"></div>
      <p class="partner"><span>The exclusive partner</span><span>for your</span><span>development projects</span></p>
      <div class="rule"></div>
      <p class="website-spaced">WWW.VORANDEL.COM</p>
    </div>
    <div class="card__band"></div>
  </section>

  <section class="card back">
    <h1 class="back__wordmark">VORANDEL</h1>
    <p class="back__motto">Excellence and reliability</p>
    <div class="person">
      <div class="rule"></div>
      <div class="person__text">
        <p class="person__name">LUCAS <b>M.REYNE</b></p>
        <p class="person__role">MANAGER</p>
      </div>
      <div class="rule"></div>
    </div>
    <div class="contact">
      <p class="contact__address">PO BOX 456 Harbor Lane<br>4th Avenue, Brisbane</p>
      <span class="contact__divider"></span>
      <ul class="contact__list">
        <li><svg viewBox="0 0 24 24" aria-hidden="true"><path d="M6.6 10.8a15.1 15.1 0 0 0 6.6 6.6l2.2-2.2c.3-.3.7-.4 1-.2 1.1.4 2.3.6 3.6.6.6 0 1 .4 1 1V20c0 .6-.4 1-1 1A17 17 0 0 1 3 4c0-.6.4-1 1-1h3.5c.6 0 1 .4 1 1 0 1.3.2 2.5.6 3.6.1.3 0 .7-.2 1z"/></svg>(+1) 555 010 2040</li>
        <li><svg viewBox="0 0 24 24" aria-hidden="true"><path d="M12 2a10 10 0 1 0 0 20 10 10 0 0 0 0-20zm6.9 6h-3a15.6 15.6 0 0 0-1.3-3.6A8 8 0 0 1 18.9 8zM12 4c.8 1.2 1.5 2.5 1.9 4h-3.8c.4-1.5 1.1-2.8 1.9-4zM4.3 14a8 8 0 0 1 0-4h3.4a16 16 0 0 0 0 4zm.8 2h3c.3 1.3.8 2.5 1.300 3.6A8 8 0 0 1 5.1 16zm3-8h-3a8 8 0 0 1 4.3-3.6C8.9 5.5 8.4 6.7 8.1 8zM12 20c-.8-1.2-1.5-2.5-1.9-4h3.8c-.4 1.5-1.1 2.8-1.9 4zm2.3-6H9.7a14.7 14.7 0 0 1 0-4h4.6a14.7 14.7 0 0 1 0 4zm.3 5.6c.5-1.1 1-2.3 1.3-3.6h3a8 8 0 0 1-4.3 3.6zm1.7-5.6a16 16 0 0 0 0-4h3.4a8 8 0 0 1 0 4z"/></svg>www.vorandel.com</li>
      </ul>
    </div>
    <div class="card__band"></div>
  </section>
</body>
</html>
```